Steady Harbor Claims Group Business card

Need a business card that stands out that includes name of company,(above) Owners name Moira Lindqvist phone#517-362-4408 email# SteadyHarborCG@mailvane.com and website www.Steadyharborclaimsgroup.net. This is a medical billing company so the card has to relate to that or relate to increasing revenue

```html
<!DOCTYPE html>
<html lang="en">
<head>
<meta charset="utf-8">
<title>Steady Harbor Claims Group – Business Card</title>
<link href="https://fonts.googleapis.com/css2?family=Cinzel:wght@500&family=Open+Sans:wght@400;700&display=swap" rel="stylesheet">
<style>
  :root {
    --brand-blue: #2e84a8;
    --brand-blue-deep: #2a7aa0;
    --brand-green: #8cc540;
    --ink: #4a4a4a;
    --rule: #d9dde0;
    --paper: #ffffff;
    --backdrop: #eceae6;
  }
  * { margin: 0; padding: 0; box-sizing: border-box; }
  html, body { width: 1200px; height: 1000px; overflow: hidden; }
  body {
    background: var(--backdrop);
    position: relative;
    font-family: "Open Sans", Arial, sans-serif;
  }
  .card {
    position: absolute;
    left: 265px;
    width: 666px;
    height: 397px;
    overflow: hidden;
    box-shadow: 0 4px 12px rgba(0,0,0,0.18);
  }
  .card--front { top: 73px; background: var(--paper); }
  .card--back { top: 532px; background: var(--brand-blue); }

  .wordmark {
    position: absolute;
    display: flex;
    align-items: center;
    gap: 12px;
    font-family: "Cinzel", Georgia, serif;
    font-weight: 500;
    line-height: 1.15;
    letter-spacing: 0.5px;
  }
  .wordmark__mark { width: 22px; height: 22px; flex: none; }
  .wordmark--front { left: 32px; top: 130px; color: var(--brand-blue); font-size: 25px; }
  .wordmark--front .wordmark__mark { background: var(--brand-green); }
  .wordmark--back {
    right: 32px; top: 278px; color: #ffffff; font-size: 25px;
    text-align: right; flex-direction: row-reverse;
  }
  .wordmark--back .wordmark__mark { background: var(--brand-green); }

  .divider {
    position: absolute; left: 32px; top: 246px;
    width: 410px; height: 1px; background: var(--rule);
  }
  .owner-name {
    position: absolute; right: 33px; top: 236px;
    color: var(--brand-blue); font-weight: 700; font-size: 19px; letter-spacing: 0.3px;
  }
  .contact-list { position: absolute; left: 32px; top: 270px; list-style: none; }
  .contact-list li {
    display: flex; align-items: center; gap: 8px;
    color: var(--ink); font-size: 16px; height: 26px;
  }
  .contact-list svg { width: 15px; height: 15px; fill: var(--brand-blue); flex: none; }

  .footer-band { position: absolute; left: 0; bottom: 0; width: 666px; height: 40px; }

  .website {
    position: absolute; right: 33px; top: 350px;
    color: #ffffff; font-size: 15px;
  }
</style>
</head>
<body>
  <section class="card card--front">
    <div class="wordmark wordmark--front">
      <span class="wordmark__mark"></span>
      <span>Steady Harbor<br>Claims Group</span>
    </div>
    <div class="divider"></div>
    <div class="owner-name">MOIRA LINDQVIST</div>
    <ul class="contact-list">
      <li>
        <svg viewBox="0 0 16 16"><path d="M2 6c0-2 2.5-3 6-3s6 1 6 3v1h-3V5.5H5V7H2z M4 8h8l1.5 5h-11z"/></svg>
        517-362-4408
      </li>
      <li>
        <svg viewBox="0 0 16 16"><path d="M1 3h14v10H1z M2 4l6 5 6-5" fill="var(--brand-blue)" stroke="#fff" stroke-width="1"/></svg>
        SteadyHarborCG@mailvane.com
      </li>
      <li>
        <svg viewBox="0 0 16 16"><circle cx="8" cy="8" r="7"/><path d="M1 8h14M8 1c3 3 3 11 0 14M8 1c-3 3-3 11 0 14" stroke="#fff" stroke-width="1" fill="none"/></svg>
        Steadyharborclaimsgroup.net
      </li>
    </ul>
    <svg class="footer-band" viewBox="0 0 666 40" preserveAspectRatio="none">
      <path d="M0 5 H330 C345 5 348 1 360 0 L362 4 C352 6 346 11 330 11 H0 Z" fill="var(--brand-green)"/>
      <path d="M0 17 H328 C352 17 356 0 392 0 H666 V40 H0 Z" fill="var(--brand-blue-deep)"/>
    </svg>
  </section>

  <section class="card card--back">
    <div class="wordmark wordmark--back">
      <span class="wordmark__mark"></span>
      <span>Steady Harbor<br>Claims Group</span>
    </div>
    <div class="website">www.steadyharborclaimsgroup.net</div>
  </section>
</body>
</html>
```